Velmora Link needs a brochure review

We are a company operating in more than 10 countries that, since 1972, has the ambitious and innovative objective to stimulate foreign language learning by discovering different countries and cultures, through training courses tailored to individual needs
We need a layout review of our brochure in order to make the content clearer, immediate and appealing and, at the same time, make the layout more modern and young.
The pages we need are: the cover and pages 3, 5, 7, 20, 21, 22, 23, 34, 36, 37. You will find our actual brochure pdf as attachment

Target Market(s)

Students and families, business

Industry/Entity Type

It Company

Requirements
Must have
• The same written information as the actual one.
• Blue and green colours.
• The cover must be simple, elegant and clean but new and effective. In addition to the cover the pages you should review are number :2, 3, 4, 5, 6, 7. Feel free to use new background, images and new layout for the text.

```html
<!DOCTYPE html>
<html lang="it">
<head>
<meta charset="utf-8">
<title>Velmora Link – Due settimane all'estero</title>
<link rel="stylesheet" href="https://fonts.googleapis.com/css2?family=Dosis:wght@500;600&family=Source+Sans+3:wght@400;600;700&display=swap">
<style>
  :root {
    --bg-top: #8fb4d8;
    --bg-mid: #d7ece6;
    --bg-bottom: #9cc8c0;
    --ink: #16283b;
    --white: #ffffff;
    --abroad: #1f5fa8;
    --italy: #2a9468;
    --row-label-a: #dde9f2;
    --row-label-b: #ffffff;
    --abroad-a: #9fc0e2;
    --abroad-b: #c4d9ef;
    --italy-a: #a8dbc4;
    --italy-b: #cdebdd;
    --total-label: #bcd2e4;
    --photo-skin: #e4cdb6;
    --photo-hair: #d8bc8c;
    --photo-book: #2f6fb4;
    --deco-a: #6f9f3c;
    --deco-z: #1e6a5a;
  }
  * { box-sizing: border-box; margin: 0; padding: 0; }
  html, body { width: 1200px; height: 2206px; overflow: hidden; }
  body {
    position: relative;
    background:
      radial-gradient(ellipse 70% 45% at 45% 50%, var(--bg-mid) 0%, rgba(215,236,230,0) 100%),
      linear-gradient(180deg, var(--bg-top) 0%, #bcd9e0 45%, var(--bg-bottom) 100%);
    color: var(--ink);
    font-family: "Dosis", sans-serif;
  }
  .page-title {
    position: absolute;
    left: 112px; top: 183px; width: 1040px;
    font-family: "Dosis", sans-serif;
    font-weight: 500;
    font-size: 43px;
    line-height: 54px;
    letter-spacing: 7.4px;
    color: var(--white);
    white-space: nowrap;
  }
  .body-copy {
    position: absolute;
    left: 112px; width: 964px;
    font-family: "Dosis", sans-serif;
    font-weight: 500;
    font-size: 20.5px;
    line-height: 29.5px;
    letter-spacing: 4.1px;
    text-align: justify;
  }
  .intro { top: 382px; }
  .school { top: 1082px; }
  .offer { top: 1238px; }
  .compare {
    position: absolute;
    left: 112px; top: 569px; width: 816px; height: 432px;
    background: var(--white);
    padding: 16px 4px 0 0;
  }
  .compare table {
    width: 100%;
    border-collapse: separate;
    border-spacing: 0 3px;
    font-family: "Source Sans 3", sans-serif;
    font-size: 26px;
  }
  .compare th, .compare td { padding: 0; text-align: center; }
  .compare td { height: 48px; }
  .compare th {
    height: 37px;
    color: var(--white);
    font-weight: 700;
    font-size: 25px;
    letter-spacing: -0.3px;
  }
  .compare th.abroad { background: var(--abroad); border-right: 4px solid var(--white); }
  .compare th.italy { background: var(--italy); }
  .compare td.label { text-align: left; padding-left: 24px; width: 447px; }
  .compare td.abroad { width: 190px; border-right: 4px solid var(--white); }
  .compare tbody tr:nth-child(odd) td.label { background: var(--row-label-a); }
  .compare tbody tr:nth-child(even) td.label { background: var(--row-label-b); }
  .compare tbody tr:nth-child(odd) td.abroad { background: var(--abroad-a); }
  .compare tbody tr:nth-child(even) td.abroad { background: var(--abroad-b); }
  .compare tbody tr:nth-child(odd) td.italy { background: var(--italy-a); }
  .compare tbody tr:nth-child(even) td.italy { background: var(--italy-b); }
  .compare tr.total td { font-weight: 700; }
  .compare tr.total td.label { background: var(--total-label) !important; }
  .compare tr.total td.abroad { background: var(--abroad) !important; color: var(--white); }
  .compare tr.total td.italy { background: var(--italy) !important; color: var(--white); }
  .illustration, .photo { position: absolute; }
  .letter-a {
    left: 30px; top: 1470px; width: 261px; height: 306px;
    border-radius: 40% 40% 30% 30%;
    background: radial-gradient(ellipse at 50% 45%, var(--deco-a) 0%, rgba(111,159,60,0.55) 45%, rgba(111,159,60,0) 72%);
  }
  .letter-z {
    left: 922px; top: 1478px; width: 257px; height: 295px;
    border-radius: 30%;
    background: radial-gradient(ellipse at 55% 45%, var(--deco-z) 0%, rgba(30,106,90,0.55) 45%, rgba(30,106,90,0) 75%);
  }
  .photo.student {
    left: 224px; top: 1515px; width: 709px; height: 557px;
    background: linear-gradient(180deg, var(--photo-hair) 0%, var(--photo-skin) 25%, var(--photo-book) 43%, #245a96 100%);
  }
</style>
</head>
<body>
  <h1 class="page-title">Perché 2 settimane all’estero equivalgono<br>ad un anno scolastico in Italia</h1>

  <p class="body-copy intro">I numeri non mentono! Durante una vacanza studio di 14 giorni all’estero, sarai esposto alla lingua straniera tanto quanto durante un intero anno a scuola in Italia, e ovviamente in modo molto più mirato ed efficiente.</p>

  <div class="compare">
    <table>
      <thead>
        <tr><th></th><th class="abroad">ALL’ ESTERO</th><th class="italy">IN ITALIA</th></tr>
      </thead>
      <tbody>
        <tr><td class="label">Giorni</td><td class="abroad">14</td><td class="italy">200</td></tr>
        <tr><td class="label">Studenti in classe</td><td class="abroad">12</td><td class="italy">25</td></tr>
        <tr><td class="label">Ore di lezione</td><td class="abroad">40</td><td class="italy">90</td></tr>
        <tr><td class="label">Ore di verifiche in classe</td><td class="abroad">-</td><td class="italy">45</td></tr>
        <tr><td class="label">Ore di attività in inglese</td><td class="abroad">100</td><td class="italy">-</td></tr>
        <tr><td class="label">Insegnanti</td><td class="abroad">Inglesi</td><td class="italy">Italiani</td></tr>
        <tr class="total"><td class="label">Totale ore di apprendimento</td><td class="abroad">140</td><td class="italy">45</td></tr>
      </tbody>
    </table>
  </div>

  <p class="body-copy school">I programmi di lingua inglese della scuola italiana prevedono circa 90 lezioni all’anno con clas-si composte da 25 studenti. Considerando le ore dedicate a verifiche e interrogazioni, il numero di lezioni effettive si riduce di circa il 50%.</p>

  <p class="body-copy offer">Una vacanza studio Velmora Link di 2 settimane prevede 20 lezioni a settimana con docenti madrelingua,sen-za verifiche o interrogazioni e in classi di non più di 15 studenti, di diverse nazionalità. Considerando che tutte le attività, anche quelle extrascolastiche, sono svolte in inglese, l’apprendimento della lingua risulta maggiore e più efficace.</p>

  <div class="illustration letter-a" role="img" aria-label="Lettera A decorativa con un fiore"></div>
  <div class="photo student" role="img" aria-label="Foto di una studentessa che legge un libro di inglese"></div>
  <div class="illustration letter-z" role="img" aria-label="Lettera Z decorativa con fiori"></div>
</body>
</html>
```